Marlow Hire Business Card for recruitment company

We are looking for a Business Card Design that incorporates our personal details and our busines name and logo. We are a specialized search consultancy that recruit Property and Construction professionals.
We would like a business card that stands out and is appealing to the Construction and Property industry as well.

Target Market(s)

people in the construction and property industry

Contact Information for Business Card

Business Name and logo

Font styles to use
Serif

Colors
0094D4
00A9DD
6FCCEA
C7EBF8
E9F6FB

Requirements
Must have
• Business name and logo as well as contact details
Should not have
• No photos of us please

```html
<!DOCTYPE html>
<html lang="en">
<head>
<meta charset="utf-8">
<title>Marlow Hire – Business Card</title>
<link rel="stylesheet" href="https://fonts.googleapis.com/css2?family=Josefin+Sans:wght@300&family=Source+Sans+3:wght@400;700&display=swap">
<style>
  :root {
    --ink: #0b3a52;
    --card-dark: #053a52;
    --card-dark-soft: #0a4660;
    --paper: #ffffff;
    --ghost: #e3e9ec;
    --stage: #d9dcdf;
  }
  * { box-sizing: border-box; margin: 0; padding: 0; }
  html, body { width: 1200px; height: 801px; overflow: hidden; }
  body {
    background: var(--stage);
    font-family: "Source Sans 3", sans-serif;
    color: var(--ink);
    position: relative;
  }
  .card {
    position: absolute;
    top: 238px;
    width: 520px;
    height: 325px;
    border-radius: 18px;
    overflow: hidden;
  }
  .card--back { left: 60px; background: var(--card-dark); }
  .card--front { left: 620px; background: var(--paper); }

  .back-pattern {
    position: absolute; inset: 0;
    background: linear-gradient(135deg, var(--card-dark-soft), var(--card-dark));
  }
  .back-brand {
    position: absolute; top: 62px; right: 48px;
    display: flex; align-items: center; gap: 10px;
    color: var(--paper);
    font-weight: 700; font-size: 18px;
  }
  .back-brand__dot {
    width: 22px; height: 22px; border-radius: 50%;
    border: 3px solid var(--paper);
  }

  .front-ghost {
    position: absolute; top: 38px; right: 34px;
    width: 112px; height: 112px; border-radius: 50%;
    border: 13px solid var(--ghost);
  }
  .wordmark {
    position: absolute; top: 104px; left: 40px;
    font-family: "Josefin Sans", sans-serif;
    font-weight: 300; font-size: 38px; letter-spacing: 1px;
    line-height: 1;
    white-space: nowrap;
    color: var(--ink);
  }
  .contact {
    position: absolute; left: 110px; top: 172px;
    font-size: 15px; line-height: 1.3;
    white-space: nowrap;
  }
  .contact__name { font-weight: 700; font-size: 21px; }
  .contact__role { font-weight: 400; }
  .contact__link { font-weight: 700; margin-bottom: 12px; }
  .contact__label { font-weight: 700; }
  .location {
    position: absolute; right: 30px; top: 176px;
    font-size: 14px;
    white-space: nowrap;
  }
</style>
</head>
<body>
  <section class="card card--back" aria-label="Card back">
    <div class="back-pattern" role="img" aria-label="Tone-on-tone repeating pattern of the brand mark"></div>
    <div class="back-brand"><span class="back-brand__dot"></span>Marlow Hire</div>
  </section>

  <section class="card card--front" aria-label="Card front">
    <div class="front-ghost"></div>
    <h1 class="wordmark">MARLOW HIRE</h1>
    <div class="contact">
      <p class="contact__name">Clara Brennick</p>
      <p class="contact__role">Director | Senior Search Consultant</p>
      <p class="contact__link">Network</p>
      <p><span class="contact__label">M:</span> +64 21 555 0142</p>
      <p><span class="contact__label">E:</span> clara@marlowhire.nz</p>
    </div>
    <p class="location">Hamilton, New Zealand</p>
  </section>
</body>
</html>
```